Psychotherapy and emotion coaching with vaLumo requires web design

I need a web design for emotion coaching (release of emotional blockages) (psychotherapy) with the target group trauma-related disorders and anxiety disorders. The website should be clear and well-organized, i.e. rather simple. The colors should be light, blue, green and yellow are desirable. The design should radiate security.

A logo already exists and should be used appropriately.

Three columns should describe the following
-Emotion regulation
-Imaginative structure constellations
-Ego-State-Therapy

An outdated draft can be seen here:
www.ruhiger-morgen.de
The website should advertise coded in Wordpress.

I need the landing page, for which there are drafts now, and at least one more page (maybe a template) for further information (like "About me")

Target Market(s)

Clients for coaching and therapy with trauma or axienty disorders;

Coding

Coded - Design and coding required

Number of Pages Required

3 page

Font styles to use
Sans Serif

Colors
0054AA
0677BA
7BADD7
CADEEF
E8F1F8
59FF00
82FF00
B8FF75
E3FFCB
F4FFEA
FFF300
FFF600
FEFA6F
FFFEC7
FFFEE8

Requirements
Nice to have
• Title: "More happiness and satisfaction in life"
Should not have
• "Therapy" should not be listed in the header; Instead "More happiness and satisfaction in life"

```html
<!DOCTYPE html>
<html lang="en">
<head>
<meta charset="utf-8">
<title>vaLumo – Web Design Pages</title>
<link href="https://fonts.googleapis.com/css2?family=Montserrat:wght@300;400;600;700;800&family=Roboto:wght@400;500;700&display=swap" rel="stylesheet">
<style>
:root{
  --board:#a7a4a5;
  --ink:#151515;
  --text:#6b6b6b;
  --blue:#3a7ff0;
  --blue-dark:#2563d6;
  --blue-soft:#cadeef;
  --navy:#0054aa;
  --yellow:#fcc70d;
  --yellow-soft:#fff3a6;
  --green:#4cbb3c;
  --green-soft:#e3ffcb;
  --footer:#f6f5f6;
  --white:#ffffff;
}
*{box-sizing:border-box;margin:0;padding:0}
html,body{width:925px;height:1200px;overflow:hidden;background:var(--board)}
body{font-family:"Roboto",sans-serif;color:var(--ink)}
.board{position:relative;width:1684px;height:2184px;transform:scale(0.5493);transform-origin:0 0}
.page{position:absolute;background:var(--white);overflow:hidden}
.page-home{left:42px;top:43px;width:514px;height:2097px}
.page-about{left:585px;top:43px;width:514px;height:1107px}
.page-blog{left:1128px;top:43px;width:514px;height:1045px}
.abs{position:absolute}

/* header */
.site-header{position:absolute;left:0;top:0;width:514px;height:50px;background:var(--white);z-index:3}
.topbar{position:absolute;left:218px;top:0;width:296px;height:19px;background:linear-gradient(90deg,#ffd21c,#f9c80e);clip-path:polygon(4% 0,100% 0,100% 100%,0 100%);display:flex;align-items:center;gap:14px;padding-left:26px;font-size:6px;font-weight:500}
.social{display:flex;gap:2px}
.social i{width:5px;height:5px;border-radius:50%;background:var(--ink);display:block}
.tb-item{display:flex;align-items:center;gap:3px}
.tb-item svg{width:6px;height:6px}
.brand{position:absolute;left:48px;top:14px;display:flex;align-items:center;gap:6px}
.brand-mark{width:18px;height:18px;background:var(--yellow);border-radius:3px}
.brand-name{font-family:"Montserrat",sans-serif;font-size:11px;font-weight:600;color:#444}
.nav-link{position:absolute;top:31px;font-size:5.5px;font-weight:700;color:var(--ink)}
.nav-link.active{color:var(--blue)}
.nav-contact{position:absolute;left:413px;top:25px;width:54px;height:18px;background:linear-gradient(180deg,#4a8df5,var(--blue-dark));clip-path:polygon(8% 0,100% 0,92% 100%,0 100%);color:#fff;font-size:5.5px;font-weight:700;display:flex;align-items:center;justify-content:center}

/* buttons */
.btn{position:absolute;height:15px;background:linear-gradient(180deg,#4a8df5,var(--blue-dark));clip-path:polygon(7% 0,100% 0,93% 100%,0 100%);color:#fff;font-size:5.3px;font-weight:700;display:flex;align-items:center;justify-content:center;gap:3px;letter-spacing:.2px}
.btn .dot{width:4px;height:4px;border-radius:50%;background:#fff}

/* headings */
.sec-title{position:absolute;left:0;width:100%;text-align:center;font-family:"Montserrat",sans-serif;font-size:15px;font-weight:400;color:var(--ink)}
.sec-title b{font-weight:800}
.sec-title::after{content:"";display:block;width:26px;height:1.5px;background:var(--blue);margin:3px auto 0}
.sec-title.left{text-align:left}
.sec-title.left::after{margin-left:0;background:var(--yellow)}
.para{font-size:6.3px;line-height:1.75;color:var(--text)}
.para.dark{color:#333}
.ticks{list-style:none}
.ticks li{position:relative;padding-left:11px;font-size:5.8px;line-height:1.8;color:var(--text);margin-bottom:6px}
.ticks li::before{content:"";position:absolute;left:0;top:2px;width:6px;height:6px;border-radius:50%;background:var(--green)}

/* hero */
.hero-home{position:absolute;left:0;top:50px;width:514px;height:262px;background:linear-gradient(100deg,#eaf8c8 0%,#f4f9e4 40%,#eef1fb 75%,#dde5fb 100%)}
.hero-art{position:absolute;left:248px;top:50px;width:266px;height:248px;background:radial-gradient(ellipse at 50% 30%,#e9a15d 0%,#d35f8e 28%,#6fb4c9 50%,rgba(236,241,240,0) 72%)}
.hero-title{position:absolute;left:48px;top:113px;font-family:"Montserrat",sans-serif;font-weight:800;font-size:15px}
.hero-sub{position:absolute;left:48px;top:139px;font-family:"Montserrat",sans-serif;font-size:12.5px;color:var(--blue)}
.hero-lead{position:absolute;left:48px;top:166px;font-size:6.5px;font-weight:700;line-height:2.1}
.hero-inner{position:absolute;left:0;top:50px;width:514px;height:196px;background:linear-gradient(90deg,#e7f2d6,#f1f0e2 50%,#e6ecf6)}
.hero-inner-title{position:absolute;left:0;width:100%;top:98px;text-align:center;font-family:"Montserrat",sans-serif;font-weight:800;font-size:17px}
.hero-inner-lead{position:absolute;left:0;width:100%;top:131px;text-align:center;font-size:6.6px;font-weight:700;line-height:2.1}
.hero-edge{position:absolute;left:0;width:514px;height:45px}

/* portrait */
.portrait{position:absolute;width:118px;height:118px;border-radius:50%;background:#f1f4fb;box-shadow:0 4px 10px rgba(60,90,150,.15)}
.portrait .photo{position:absolute;left:13px;top:13px;width:92px;height:92px;border-radius:50%;background:radial-gradient(circle at 50% 40%,#d9c4b3,#7c8694 70%,#2f4a3a)}
.chevron{position:absolute;width:143px;height:47px}

/* specialize cards */
.spec-band{position:absolute;left:0;top:547px;width:514px;height:645px;background:linear-gradient(180deg,#f2f2f5,#f6f6f8)}
.spec-card{position:absolute;left:73px;width:366px;height:159px;border-radius:10px;border:1.5px solid}
.spec-card.yellow{top:620px;background:linear-gradient(90deg,#fffbe8,#fff2b8 55%,#ffd43f);border-color:#f3c300}
.spec-card.green{top:791px;background:linear-gradient(90deg,#56b847,#a8ec8e 45%,#e5fbdb);border-color:#79cf63}
.spec-card.blue{top:960px;background:linear-gradient(90deg,#f4f6ff,#dfe7ff 60%,#5c8ff1);border-color:#5c8ff1}
.spec-frame{position:absolute;left:66px;width:382px;height:171px;border:1px dashed #b8b8bf;border-radius:12px}
.spec-img{position:absolute;top:9px;width:160px;height:140px;border-radius:10px}
.spec-name{position:absolute;font-family:"Montserrat",sans-serif;font-weight:700;font-size:14px;line-height:1.45;letter-spacing:.5px}
.spec-text{position:absolute;font-size:5.3px;line-height:1.95;color:#6b6b6b}

/* treatment */
.treat-card{position:absolute;top:1259px;width:149px;height:159px;background:#fff;box-shadow:0 2px 8px rgba(0,0,0,.15)}
.treat-card.hl{border:1px solid #e6d66b;box-shadow:0 2px 8px rgba(60,110,220,.3)}
.treat-img{position:absolute;left:3px;top:3px;width:143px;height:83px}
.treat-icon{position:absolute;left:58px;top:67px;width:32px;height:32px;border-radius:50%;border:3px solid #fff}
.treat-name{position:absolute;left:0;width:100%;top:104px;text-align:center;font-size:6.5px;font-weight:700}
.treat-text{position:absolute;left:14px;width:121px;top:118px;text-align:center;font-size:5.5px;line-height:1.85;color:var(--text)}

/* testimonials */
.testi{position:absolute;top:1505px;width:131px;height:87px;background:#fff;box-shadow:0 2px 6px rgba(0,0,0,.12);border-bottom:1.5px solid #333}
.testi.mid{border-bottom-color:var(--green)}
.testi-avatar{position:absolute;left:10px;top:-10px;width:26px;height:26px;border-radius:50%;background:radial-gradient(circle at 50% 40%,#c9b3a2,#506070);border:2px solid #fff}
.testi-name{position:absolute;left:46px;top:5px;font-size:6px;font-weight:700}
.stars{position:absolute;left:46px;top:15px;display:flex;gap:1.5px}
.stars i{width:4px;height:4px;background:#f05a1a;clip-path:polygon(50% 0,62% 38%,100% 38%,69% 60%,80% 100%,50% 76%,20% 100%,31% 60%,0 38%,38% 38%)}
.testi-text{position:absolute;left:14px;top:28px;width:108px;font-size:5px;line-height:2;color:var(--text)}
.arrow-btn{position:absolute;top:1539px;width:15px;height:15px;border-radius:50%;display:flex;align-items:center;justify-content:center}

/* contact */
.contact-band{position:absolute;left:0;top:1630px;width:514px;height:300px;background:linear-gradient(100deg,#edf8d8,#faf6e4 50%,#e8ecfa)}
.field{position:absolute;height:25px;background:#fff;border-radius:3px;box-shadow:0 1px 4px rgba(0,0,0,.08);font-size:5.5px;color:#777;padding:9px 10px}
.field.select::after{content:"";position:absolute;right:12px;top:10px;width:3px;height:3px;border-right:1px solid #777;border-bottom:1px solid #777;transform:rotate(45deg)}

/* blog */
.post{position:absolute;width:123px;height:152px;background:#fff;box-shadow:0 1px 6px rgba(0,0,0,.13);border-radius:4px}
.post-img{position:absolute;left:3px;top:3px;width:117px;height:84px;border-radius:4px}
.post-plus{position:absolute;left:101px;top:78px;width:12px;height:12px;border-radius:50%;background:var(--blue);color:#fff;font-size:8px;line-height:12px;text-align:center}
.post-meta{position:absolute;left:8px;top:93px;display:flex;gap:14px;font-size:4.8px;color:#777}
.post-meta span{display:flex;align-items:center;gap:3px}
.post-meta span::before{content:"";width:4px;height:4px;background:var(--yellow);border-radius:1px}
.post-title{position:absolute;left:8px;top:104px;width:108px;font-size:5.6px;font-weight:700;line-height:1.75}
.post-text{position:absolute;left:8px;top:126px;width:108px;font-size:5.2px;line-height:1.8;color:var(--text)}
.pager-line{position:absolute;left:94px;top:802px;width:326px;height:1px;background:#ccc}
.pager{position:absolute;top:797px;width:11px;height:11px;border-radius:50%;background:#fff;border:1px solid #bbb;font-size:5px;text-align:center;line-height:9px}

/* footer */
.site-footer{position:absolute;left:0;width:514px;height:215px}
.footer-edge{position:absolute;left:0;top:0;width:514px;height:215px}
.footer-mark{position:absolute;left:247px;top:24px;width:20px;height:20px;background:var(--yellow);border-radius:3px}
.footer-nav{position:absolute;left:0;width:100%;top:74px;display:flex;justify-content:center;gap:14px;font-size:5.5px;color:#333}
.f-contact{position:absolute;top:105px;display:flex;gap:7px}
.f-icon{width:15px;height:15px;border-radius:50%;background:#fff;box-shadow:0 1px 4px rgba(0,0,0,.15);display:flex;align-items:center;justify-content:center;margin-top:5px}
.f-icon svg{width:6px;height:6px}
.f-label{font-size:5px;color:#444}
.f-value{font-size:7px;font-weight:500;line-height:1.5;margin-top:2px}
.f-news-label{position:absolute;left:68px;top:152px;font-size:5.3px;font-weight:700}
.f-news{position:absolute;left:68px;top:165px;width:213px;height:17px;background:#fff;box-shadow:0 1px 4px rgba(0,0,0,.1);font-size:4.8px;letter-spacing:3px;color:#777;padding:6px 10px}
.f-news-go{position:absolute;right:2px;top:2px;width:13px;height:13px;background:var(--blue)}
.f-media{position:absolute;left:398px;top:163px;display:flex;align-items:center;gap:10px;font-size:5px;font-weight:700}
.f-copy{position:absolute;left:339px;top:177px;font-size:4.8px;color:#333}
</style>
</head>
<body>
<div class="board">

<!-- ============ HOME PAGE ============ -->
<section class="page page-home">
  <header class="site-header">
    <div class="topbar">
      <span class="social"><i></i><i></i><i></i></span>
      <span class="tb-item"><svg viewBox="0 0 10 10"><path d="M2 1l2 0 1 2.5-1.2 1a5 5 0 0 0 2.7 2.7l1-1.2L10 7v2a1 1 0 0 1-1 1A9 9 0 0 1 0 2a1 1 0 0 1 1-1z" fill="#151515"/></svg>0160 482 39 117</span>
      <span class="tb-item"><svg viewBox="0 0 10 10"><rect x="0" y="2" width="10" height="6.5" fill="#151515"/><path d="M0 2l5 3.5L10 2" stroke="#ffd21c" stroke-width="1" fill="none"/></svg>info@valumo-praxis.de</span>
    </div>
    <div class="brand"><span class="brand-mark"></span><span class="brand-name">vaLumo</span></div>
    <span class="nav-link active" style="left:188px">HOME</span>
    <span class="nav-link" style="left:224px">ABOUT US</span>
    <span class="nav-link" style="left:271px">SERVICES</span>
    <span class="nav-link" style="left:317px">TESTIMONIALS</span>
    <span class="nav-link" style="left:378px">BLOG</span>
    <span class="nav-contact">CONTACT US</span>
  </header>

  <div class="hero-home"></div>
  <div class="hero-art" role="img" aria-label="Illustration of a colourful tree growing in the shape of a brain"></div>
  <h1 class="hero-title">LET GO OF BURDENS!</h1>
  <p class="hero-sub">FIND MORE JOY IN LIFE!</p>
  <p class="hero-lead">I REGRET HAVING TO HELP YOU WITH EMOTIONAL<br>DISTRESS ORTO SUPPORT IN CRISES</p>
  <span class="btn" style="left:48px;top:203px;width:68px">GET STARTED <i class="dot"></i></span>
  <svg class="hero-edge" style="top:270px" viewBox="0 0 514 45"><polygon points="0,5 257,40 514,5 514,45 0,45" fill="#fff"/><polyline points="0,5 257,40 514,5" fill="none" stroke="#f7c10c" stroke-width="3"/></svg>

  <div class="portrait" style="left:82px;top:351px"><div class="photo" role="img" aria-label="Portrait photo of the therapist"></div></div>
  <svg class="chevron" style="left:71px;top:455px" viewBox="0 0 143 47"><polygon points="0,0 71,28 143,0 143,19 71,47 0,19" fill="#3a7ff0"/><polygon points="0,0 71,28 143,0 143,6 71,34 0,6" fill="#8fb6f7"/></svg>
  <svg class="abs" style="left:137px;top:500px" width="120" height="120"><path d="M1 0V115H120" fill="none" stroke="#9a9aa3" stroke-dasharray="2 2"/></svg>
  <h2 class="sec-title left" style="left:258px;top:345px;width:200px">ABOUT <span style="font-weight:400">US</span></h2>
  <p class="para dark abs" style="left:258px;top:374px;width:200px">If you have just reached one of the following points in life, I would be happy to support you in finding ways out ofthe crisis and bring about change:</p>
  <ul class="ticks abs" style="left:258px;top:419px;width:200px">
    <li>You or someone close to you has been diagnosed with a serious illness such as cance</li>
    <li>You or someone close to you has been diagnosed with a serious illness such as cance</li>
  </ul>
  <span class="btn" style="left:258px;top:480px;width:67px;height:17px">VIEW MORE <i class="dot"></i></span>

  <div class="spec-band"></div>
  <h2 class="sec-title" style="top:580px"><b>OUR</b> SPECIALIZE <b>IN</b></h2>

  <div class="spec-frame" style="top:614px"></div>
  <div class="spec-card yellow">
    <div class="spec-img" style="left:197px;background:linear-gradient(135deg,#2b1a55,#7a2d8c 50%,#e0469c)" role="img" aria-label="Photo of a face dissolving into glowing coloured smoke"></div>
    <h3 class="spec-name" style="left:24px;top:22px">EMOTION<br>REGULATION</h3>
    <p class="spec-text" style="left:24px;top:66px;width:160px">Lorem ipsum dolor sit amet, consectetur adipiscing elit, sed do eiusmod tempor incididunt ut labore et dolore magna aliqua. Quis ipsum suspendisse ultrices gravida. Risus commodo viverra maecenas accumsan lacus vel facilisis.</p>
    <span class="btn" style="left:24px;top:119px;width:68px">VIEW MORE <i class="dot"></i></span>
  </div>

  <div class="spec-frame" style="top:784px"></div>
  <div class="spec-card green">
    <div class="spec-img" style="left:6px;background:linear-gradient(135deg,#152043,#3a3f6a 45%,#c8672b)" role="img" aria-label="Photo of glowing molecule chains in space"></div>
    <h3 class="spec-name" style="left:193px;top:20px">IMAGINATIVE<br>STRUCTURE<br>CONSTELLATIONS</h3>
    <p class="spec-text" style="left:193px;top:85px;width:160px">Lorem ipsum dolor sit amet, consectetur adipiscing elit, sed do eiusmod tempor incididunt ut labore</p>
    <span class="btn" style="left:197px;top:116px;width:68px">VIEW MORE <i class="dot"></i></span>
  </div>

  <div class="spec-frame" style="top:953px"></div>
  <div class="spec-card blue">
    <div class="spec-img" style="left:197px;background:linear-gradient(180deg,#f3c08d,#b98b72 45%,#3d5877)" role="img" aria-label="Photo of balanced stones on calm water at sunset"></div>
    <h3 class="spec-name" style="left:24px;top:22px">EGO-STATE-<br>THERAPHY</h3>
    <p class="spec-text" style="left:24px;top:64px;width:160px">Lorem ipsum dolor sit amet, consectetur adipiscing elit, sed do eiusmod tempor incididunt ut labore et dolore magna aliqua. Quis ipsum suspendisse ultrices gravida. Risus commodo viverra maecenas accumsan lacus vel facilisis.</p>
    <span class="btn" style="left:24px;top:117px;width:68px">VIEW MORE <i class="dot"></i></span>
  </div>
  <span class="btn" style="left:224px;top:1140px;width:67px">GET STARTED <i class="dot"></i></span>

  <h2 class="sec-title" style="top:1225px"><b>PSYCHOTHERAPY</b> TREATMENT</h2>
  <div class="treat-card" style="left:102px">
    <div class="treat-img" style="background:linear-gradient(180deg,#3a4f6a,#c4552a 55%,#5a3a2a)" role="img" aria-label="Photo of a head silhouette with fiery clouds"></div>
    <div class="treat-icon" style="background:#4a8df5"></div>
    <p class="treat-name">TRAUMA-RELATED DISORDERS</p>
    <p class="treat-text">Lorem ipsum dolor sit amet, consectetur adipiscing elit, sed do eiusmod tempor incididunt ut labore et</p>
  </div>
  <div class="treat-card hl" style="left:264px">
    <div class="treat-img" style="background:linear-gradient(135deg,#0d3a6e,#2f8fd6 50%,#123055)" role="img" aria-label="Photo of glowing blue nerve cells"></div>
    <div class="treat-icon" style="background:#4cbb3c"></div>
    <p class="treat-name">ANXIETY DISORDERS</p>
    <p class="treat-text">Lorem ipsum dolor sit amet, consectetur adipiscing elit, sed do eiusmod tempor incididunt ut labore et</p>
  </div>

  <h2 class="sec-title" style="top:1457px"><b>OUR</b> TESTIIMONIALS</h2>
  <span class="arrow-btn" style="left:21px;background:#fff;box-shadow:0 1px 4px rgba(0,0,0,.2)"><svg width="6" height="6" viewBox="0 0 6 6"><path d="M4 0.5L1.5 3 4 5.5" stroke="#222" stroke-width="1.3" fill="none"/></svg></span>
  <div class="testi" style="left:48px"><div class="testi-avatar" role="img" aria-label="Client photo"></div><p class="testi-name">JHON MIKE</p><span class="stars"><i></i><i></i><i></i><i></i><i></i></span><p class="testi-text">Lorem ipsum dolor sit amet, sectetur adipiscing elit, sed do eiusmod por incididunt ut labore et dolore magna aliqua. Ut enim ad minim veniam, quis nostrud</p></div>
  <div class="testi mid" style="left:191px"><div class="testi-avatar" role="img" aria-label="Client photo"></div><p class="testi-name">JHON MIKE</p><span class="stars"><i></i><i></i><i></i><i></i><i></i></span><p class="testi-text">Lorem ipsum dolor sit amet, sectetur adipiscing elit, sed do eiusmod por incididunt ut labore et dolore magna aliqua. Ut enim ad minim veniam, quis nostrud</p></div>
  <div class="testi" style="left:335px"><div class="testi-avatar" role="img" aria-label="Client photo"></div><p class="testi-name">JHON MIKE</p><span class="stars"><i></i><i></i><i></i><i></i><i></i></span><p class="testi-text">Lorem ipsum dolor sit amet, sectetur adipiscing elit, sed do eiusmod por incididunt ut labore et dolore magna aliqua. Ut enim ad minim veniam, quis nostrud</p></div>
  <span class="arrow-btn" style="left:478px;background:var(--green)"><svg width="6" height="6" viewBox="0 0 6 6"><path d="M2 0.5L4.5 3 2 5.5" stroke="#fff" stroke-width="1.3" fill="none"/></svg></span>

  <div class="contact-band"></div>
  <h2 class="sec-title" style="top:1658px"><b>CONTACT</b> US</h2>
  <p class="abs" style="left:0;width:100%;top:1694px;text-align:center;font-size:5.8px;font-weight:700">THE INITIAL CONSULTATION, WHICH LASTS APPROXIMATELY <span style="color:var(--navy)">45 MINUTES, IS FREE OF CHARGE</span></p>
  <div class="field" style="left:108px;top:1719px;width:146px">Name</div>
  <div class="field" style="left:260px;top:1719px;width:146px">Email</div>
  <div class="field" style="left:108px;top:1749px;width:146px">Phone</div>
  <div class="field select" style="left:260px;top:1749px;width:146px;color:#333">Treatment</div>
  <div class="field" style="left:108px;top:1779px;width:298px;height:43px">Message</div>
  <span class="btn" style="left:224px;top:1834px;width:67px">SUBMIT</span>

  <footer class="site-footer" style="top:1887px">
    <svg class="footer-edge" viewBox="0 0 514 215"><polygon points="0,35 257,0 514,35 514,215 0,215" fill="#f6f5f6"/><polyline points="0,35 257,0 514,35" fill="none" stroke="#f7c10c" stroke-width="3"/></svg>
    <span class="footer-mark"></span>
    <nav class="footer-nav"><span>HOME</span><span>ABOUT US</span><span>SERVICES</span><span>TESTIMONIALS</span><span>BLOG</span><span>CONTACT</span></nav>
    <div class="f-contact" style="left:63px"><span class="f-icon"><svg viewBox="0 0 10 10"><path d="M2 1l2 0 1 2.5-1.2 1a5 5 0 0 0 2.7 2.7l1-1.2L10 7v2a1 1 0 0 1-1 1A9 9 0 0 1 0 2a1 1 0 0 1 1-1z" fill="#151515"/></svg></span><div><p class="f-label">CALL US</p><p class="f-value">0160 482 39 117</p></div></div>
    <div class="f-contact" style="left:211px"><span class="f-icon"><svg viewBox="0 0 10 10"><rect x="0" y="2" width="10" height="6.5" fill="#151515"/><path d="M0 2l5 3.5L10 2" stroke="#fff" stroke-width="1" fill="none"/></svg></span><div><p class="f-label">EMAIL US</p><p class="f-value">info@valumo-praxis.de</p></div></div>
    <div class="f-contact" style="left:358px"><span class="f-icon"><svg viewBox="0 0 10 10"><path d="M5 0a3.5 3.5 0 0 1 3.5 3.5C8.5 6 5 10 5 10S1.5 6 1.5 3.5A3.5 3.5 0 0 1 5 0z" fill="#151515"/><circle cx="5" cy="3.5" r="1.2" fill="#fff"/></svg></span><div><p class="f-label">LOCATION</p><p class="f-value">Jonas Feldmann<br>Lindenweg 12<br>38100 Musterstadt</p></div></div>
    <p class="f-news-label">SUBSCRIBE TO OUR NEWSLETTER</p>
    <div class="f-news">ENTER YOUR NEWSLETTER<span class="f-news-go"></span></div>
    <div class="f-media">MEDIA <span class="social"><i></i><i></i><i></i></span></div>
    <p class="f-copy">Copyright@2024 All Rights By ruhiger-morgen</p>
  </footer>
</section>

<!-- ============ ABOUT PAGE ============ -->
<section class="page page-about">
  <header class="site-header">
    <div class="topbar">
      <span class="social"><i></i><i></i><i></i></span>
      <span class="tb-item"><svg viewBox="0 0 10 10"><path d="M2 1l2 0 1 2.5-1.2 1a5 5 0 0 0 2.7 2.7l1-1.2L10 7v2a1 1 0 0 1-1 1A9 9 0 0 1 0 2a1 1 0 0 1 1-1z" fill="#151515"/></svg>0160 482 39 117</span>
      <span class="tb-item"><svg viewBox="0 0 10 10"><rect x="0" y="2" width="10" height="6.5" fill="#151515"/><path d="M0 2l5 3.5L10 2" stroke="#ffd21c" stroke-width="1" fill="none"/></svg>info@valumo-praxis.de</span>
    </div>
    <div class="brand"><span class="brand-mark"></span><span class="brand-name">vaLumo</span></div>
    <span class="nav-link" style="left:188px">HOME</span>
    <span class="nav-link active" style="left:224px">ABOUT US</span>
    <span class="nav-link" style="left:271px">SERVICES</span>
    <span class="nav-link" style="left:317px">TESTIMONIALS</span>
    <span class="nav-link" style="left:378px">BLOG</span>
    <span class="nav-contact">CONTACT US</span>
  </header>

  <div class="hero-inner" role="img" aria-label="Photo of an open hand beneath a faint glowing brain"></div>
  <h1 class="hero-inner-title">ABOUT US</h1>
  <p class="hero-inner-lead">LOREM IPSUM DOLOR SIT AMET, CONSECTETUR ADIPISCING ELIT, SED<br>DO EIUSMOD TEMPOR INCIDIDUNT UT LABORE</p>
  <span class="btn" style="left:224px;top:168px;width:66px">GET STARTED <i class="dot"></i></span>
  <svg class="hero-edge" style="top:200px;height:50px" viewBox="0 0 514 50"><polygon points="0,7 257,44 514,7 514,50 0,50" fill="#fff"/><polyline points="0,7 257,44 514,7" fill="none" stroke="#f7c10c" stroke-width="3"/></svg>

  <div class="portrait" style="left:85px;top:271px"><div class="photo" role="img" aria-label="Portrait photo of the therapist"></div></div>
  <svg class="chevron" style="left:71px;top:375px" viewBox="0 0 143 47"><polygon points="0,0 71,28 143,0 143,19 71,47 0,19" fill="#3a7ff0"/><polygon points="0,0 71,28 143,0 143,6 71,34 0,6" fill="#8fb6f7"/></svg>
  <p class="para dark abs" style="left:263px;top:274px;width:205px">If you have just reached one of the following points in life, I would be happy to support you in finding ways out ofthe crisis and bring about change:</p>
  <ul class="ticks abs" style="left:263px;top:318px;width:205px">
    <li>You or someone close to you has been diagnosed with a serious illness such as cance</li>
    <li>You suffer from fears, phobias or illnesses such as tinnitus</li>
    <li>You have had bad or traumatic experiences and/or are suffering from their consequences or from post-traumaticStress disorder</li>
    <li>You are having difficulties at work or with your partner.</li>
    <li>You are in a crisis or situation of upheaval</li>
  </ul>
  <div class="para abs" style="left:49px;top:434px;width:420px">
    <p style="margin-bottom:6px">I accompany and encourage you to recognize and abandon outdated beliefs and replace them with new, powerful ones.</p>
    <p style="margin-bottom:6px">We would be happy to discuss the details in a preliminary meeting. On the following pages I would like to give you information about my offer and the methods that I use based on my owni have learned to know and appreciate experience.</p>
    <p>For further information please do not hesitate to contact me - Jonas</p>
  </div>

  <h2 class="sec-title" style="top:519px"><b>ABOUT</b> EMDR</h2>
  <div class="para abs" style="left:49px;top:565px;width:192px;font-size:5.6px">
    <p style="margin-bottom:7px">Lorem ipsum dolor sit amet, consectetur adipiscing elit, sed do eiusmod tempor incididunt ut labore et dolore magna aliqua. Ut enim ad minim veniam, quis nostrud exercitation ullamco laboris nisi ut aliquip ex ea commodo consequat. Duis aute irure dolor in reprehenderit in voluptate velit esse cillum dolore eu fugiat nulla pariatur. Excepteur sint occaecat cupidatat non proident, sunt in culpa qui officia deserunt mollit anim id est laborum.</p>
    <p>Lorem ipsum dolor sit amet, consectetur adipiscing elit, sed do eiusmod tempor incididunt ut labore et dolore magna aliqua. Ut enim ad minim veniam, quis nostrud exercitation ullamco laboris nisi ut aliquip ex ea commodo consequat. Duis aute irure</p>
  </div>
  <div class="abs" style="left:273px;top:555px;width:193px;height:146px;background:linear-gradient(135deg,#f2c4ae,#e9b29a 50%,#5e9a8a)" role="img" aria-label="Illustration of a watering can nurturing a brain and a growing plant"></div>
  <div class="abs" style="left:48px;top:716px;width:193px;height:146px;background:radial-gradient(circle at 50% 50%,#e8624f 0%,#edb79f 35%,#f0c7b2 100%)" role="img" aria-label="Diagram of the EMDR process around a head silhouette: eye, movement, desensitisation and reprocessing"></div>
  <div class="para abs" style="left:273px;top:733px;width:193px;font-size:5.6px">
    <p style="margin-bottom:7px">Lorem ipsum dolor sit amet, consectetur adipiscing elit, sed do eiusmod tempor incididunt ut labore et dolore magna aliqua. Ut enim ad minim veniam, quis nostrud exercitation ullamco laboris nisi ut aliquip ex ea commodo consequat. Duis aute irure dolor in reprehenderit in voluptate velit esse cillum dolore eu fugiat nulla pariatur. Excepteur sint occaecat cupidatat non proident, sunt in culpa q</p>
    <p>Lorem ipsum dolor sit amet, consectetur adipiscing elit, sed do eiusmod tempor incididunt ut labore et dolore magna aliqua. Ut enim ad minim veniam, quis nostrud exercitation</p>
  </div>

  <footer class="site-footer" style="top:899px">
    <svg class="footer-edge" viewBox="0 0 514 215"><polygon points="0,35 257,0 514,35 514,215 0,215" fill="#f6f5f6"/><polyline points="0,35 257,0 514,35" fill="none" stroke="#f7c10c" stroke-width="3"/></svg>
    <span class="footer-mark"></span>
    <nav class="footer-nav"><span>HOME</span><span>ABOUT US</span><span>SERVICES</span><span>TESTIMONIALS</span><span>BLOG</span><span>CONTACT</span></nav>
    <div class="f-contact" style="left:63px"><span class="f-icon"><svg viewBox="0 0 10 10"><path d="M2 1l2 0 1 2.5-1.2 1a5 5 0 0 0 2.7 2.7l1-1.2L10 7v2a1 1 0 0 1-1 1A9 9 0 0 1 0 2a1 1 0 0 1 1-1z" fill="#151515"/></svg></span><div><p class="f-label">CALL US</p><p class="f-value">0160 482 39 117</p></div></div>
    <div class="f-contact" style="left:211px"><span class="f-icon"><svg viewBox="0 0 10 10"><rect x="0" y="2" width="10" height="6.5" fill="#151515"/><path d="M0 2l5 3.5L10 2" stroke="#fff" stroke-width="1" fill="none"/></svg></span><div><p class="f-label">EMAIL US</p><p class="f-value">info@valumo-praxis.de</p></div></div>
    <div class="f-contact" style="left:358px"><span class="f-icon"><svg viewBox="0 0 10 10"><path d="M5 0a3.5 3.5 0 0 1 3.5 3.5C8.5 6 5 10 5 10S1.5 6 1.5 3.5A3.5 3.5 0 0 1 5 0z" fill="#151515"/><circle cx="5" cy="3.5" r="1.2" fill="#fff"/></svg></span><div><p class="f-label">LOCATION</p><p class="f-value">Jonas Feldmann<br>Lindenweg 12<br>38100 Musterstadt</p></div></div>
    <p class="f-news-label">SUBSCRIBE TO OUR NEWSLETTER</p>
    <div class="f-news">ENTER YOUR NEWSLETTER<span class="f-news-go"></span></div>
    <div class="f-media">MEDIA <span class="social"><i></i><i></i><i></i></span></div>
    <p class="f-copy">Copyright@2024 All Rights By ruhiger-morgen</p>
  </footer>
</section>

<!-- ============ BLOG PAGE ============ -->
<section class="page page-blog">
  <header class="site-header">
    <div class="topbar">
      <span class="social"><i></i><i></i><i></i></span>
      <span class="tb-item"><svg viewBox="0 0 10 10"><path d="M2 1l2 0 1 2.5-1.2 1a5 5 0 0 0 2.7 2.7l1-1.2L10 7v2a1 1 0 0 1-1 1A9 9 0 0 1 0 2a1 1 0 0 1 1-1z" fill="#151515"/></svg>0160 482 39 117</span>
      <span class="tb-item"><svg viewBox="0 0 10 10"><rect x="0" y="2" width="10" height="6.5" fill="#151515"/><path d="M0 2l5 3.5L10 2" stroke="#ffd21c" stroke-width="1" fill="none"/></svg>info@valumo-praxis.de</span>
    </div>
    <div class="brand"><span class="brand-mark"></span><span class="brand-name">vaLumo</span></div>
    <span class="nav-link" style="left:188px">HOME</span>
    <span class="nav-link" style="left:224px">ABOUT US</span>
    <span class="nav-link" style="left:271px">SERVICES</span>
    <span class="nav-link" style="left:317px">TESTIMONIALS</span>
    <span class="nav-link active" style="left:378px">BLOG</span>
    <span class="nav-contact">CONTACT US</span>
  </header>

  <div class="hero-inner" role="img" aria-label="Photo of an open hand beneath a faint glowing brain"></div>
  <h1 class="hero-inner-title">OUR BLOG</h1>
  <p class="hero-inner-lead">LOREM IPSUM DOLOR SIT AMET, CONSECTETUR ADIPISCING ELIT, SED<br>DO EIUSMOD TEMPOR INCIDIDUNT UT LABORE</p>
  <span class="btn" style="left:224px;top:168px;width:66px">GET STARTED <i class="dot"></i></span>
  <svg class="hero-edge" style="top:200px;height:50px" viewBox="0 0 514 50"><polygon points="0,7 257,44 514,7 514,50 0,50" fill="#fff"/><polyline points="0,7 257,44 514,7" fill="none" stroke="#f7c10c" stroke-width="3"/></svg>

  <article class="post" style="left:56px;top:277px"><div class="post-img" style="background:linear-gradient(135deg,#cfc7c2,#8a8f9a)" role="img" aria-label="Photo of two women talking on a sofa"></div><span class="post-plus">+</span><div class="post-meta"><span>June 24,2024</span><span>By Admin</span></div><p class="post-title">Lorem ipsum dolor sit amet, consec tetur adipiscing</p><p class="post-text">ed ut perspiciatis unde omnis iste natus error sit voluptatem accusantium</p></article>
  <article class="post" style="left:195px;top:277px"><div class="post-img" style="background:linear-gradient(135deg,#efe7e2,#2b2623)" role="img" aria-label="Photo of a head silhouette with a window inside"></div><span class="post-plus">+</span><div class="post-meta"><span>June 24,2024</span><span>By Admin</span></div><p class="post-title">Lorem ipsum dolor sit amet, consec tetur adipiscing</p><p class="post-text">ed ut perspiciatis unde omnis iste natus error sit voluptatem accusantium</p></article>
  <article class="post" style="left:334px;top:277px"><div class="post-img" style="background:linear-gradient(135deg,#f0a25a,#5b8fb8)" role="img" aria-label="Photo of a person with closed eyes in warm light"></div><span class="post-plus">+</span><div class="post-meta"><span>June 24,2024</span><span>By Admin</span></div><p class="post-title">Lorem ipsum dolor sit amet, consec tetur adipiscing</p><p class="post-text">ed ut perspiciatis unde omnis iste natus error sit voluptatem accusantium</p></article>

  <article class="post" style="left:56px;top:451px"><div class="post-img" style="background:linear-gradient(135deg,#3a2a24,#b4644a)" role="img" aria-label="Photo of a woman sitting in a group session"></div><span class="post-plus">+</span><div class="post-meta"><span>June 24,2024</span><span>By Admin</span></div><p class="post-title">Lorem ipsum dolor sit amet, consec tetur adipiscing</p><p class="post-text">ed ut perspiciatis unde omnis iste natus error sit voluptatem accusantium</p></article>
  <article class="post" style="left:195px;top:451px"><div class="post-img" style="background:linear-gradient(135deg,#e0b070,#5a4a3a)" role="img" aria-label="Photo of stacked stones in autumn light"></div><span class="post-plus">+</span><div class="post-meta"><span>June 24,2024</span><span>By Admin</span></div><p class="post-title">Lorem ipsum dolor sit amet, consec tetur adipiscing</p><p class="post-text">ed ut perspiciatis unde omnis iste natus error sit voluptatem accusantium</p></article>
  <article class="post" style="left:334px;top:451px"><div class="post-img" style="background:linear-gradient(135deg,#9a9ea3,#4f7a3a)" role="img" aria-label="Photo of a tree losing leaves in the wind"></div><span class="post-plus">+</span><div class="post-meta"><span>June 24,2024</span><span>By Admin</span></div><p class="post-title">Lorem ipsum dolor sit amet, consec tetur adipiscing</p><p class="post-text">ed ut perspiciatis unde omnis iste natus error sit voluptatem accusantium</p></article>

  <article class="post" style="left:56px;top:623px"><div class="post-img" style="background:linear-gradient(135deg,#d8dde0,#6a9a4a)" role="img" aria-label="Photo of a tree shaped like a head"></div><span class="post-plus">+</span><div class="post-meta"><span>June 24,2024</span><span>By Admin</span></div><p class="post-title">Lorem ipsum dolor sit amet, consec tetur adipiscing</p><p class="post-text">ed ut perspiciatis unde omnis iste natus error sit voluptatem accusantium</p></article>
  <article class="post" style="left:195px;top:623px"><div class="post-img" style="background:linear-gradient(135deg,#2a2a2c,#8a6a5a)" role="img" aria-label="Photo of two people holding hands"></div><span class="post-plus">+</span><div class="post-meta"><span>June 24,2024</span><span>By Admin</span></div><p class="post-title">Lorem ipsum dolor sit amet, consec tetur adipiscing</p><p class="post-text">ed ut perspiciatis unde omnis iste natus error sit voluptatem accusantium</p></article>
  <article class="post" style="left:334px;top:623px"><div class="post-img" style="background:linear-gradient(180deg,#d9c2b0,#e36a2a 55%,#2a1e1a)" role="img" aria-label="Photo of a head silhouette over a sunset sea"></div><span class="post-plus">+</span><div class="post-meta"><span>June 24,2024</span><span>By Admin</span></div><p class="post-title">Lorem ipsum dolor sit amet, consec tetur adipiscing</p><p class="post-text">ed ut perspiciatis unde omnis iste natus error sit voluptatem accusantium</p></article>

  <div class="pager-line"></div>
  <span class="pager" style="left:229px">1</span>
  <span class="pager" style="left:244px">2</span>
  <span class="pager" style="left:259px">3</span>
  <span class="pager" style="left:275px">4</span>

  <footer class="site-footer" style="top:834px">
    <svg class="footer-edge" viewBox="0 0 514 215"><polygon points="0,35 257,0 514,35 514,215 0,215" fill="#f6f5f6"/><polyline points="0,35 257,0 514,35" fill="none" stroke="#f7c10c" stroke-width="3"/></svg>
    <span class="footer-mark"></span>
    <nav class="footer-nav"><span>HOME</span><span>ABOUT US</span><span>SERVICES</span><span>TESTIMONIALS</span><span>BLOG</span><span>CONTACT</span></nav>
    <div class="f-contact" style="left:63px"><span class="f-icon"><svg viewBox="0 0 10 10"><path d="M2 1l2 0 1 2.5-1.2 1a5 5 0 0 0 2.7 2.7l1-1.2L10 7v2a1 1 0 0 1-1 1A9 9 0 0 1 0 2a1 1 0 0 1 1-1z" fill="#151515"/></svg></span><div><p class="f-label">CALL US</p><p class="f-value">0160 482 39 117</p></div></div>
    <div class="f-contact" style="left:211px"><span class="f-icon"><svg viewBox="0 0 10 10"><rect x="0" y="2" width="10" height="6.5" fill="#151515"/><path d="M0 2l5 3.5L10 2" stroke="#fff" stroke-width="1" fill="none"/></svg></span><div><p class="f-label">EMAIL US</p><p class="f-value">info@valumo-praxis.de</p></div></div>
    <div class="f-contact" style="left:358px"><span class="f-icon"><svg viewBox="0 0 10 10"><path d="M5 0a3.5 3.5 0 0 1 3.5 3.5C8.5 6 5 10 5 10S1.5 6 1.5 3.5A3.5 3.5 0 0 1 5 0z" fill="#151515"/><circle cx="5" cy="3.5" r="1.2" fill="#fff"/></svg></span><div><p class="f-label">LOCATION</p><p class="f-value">Jonas Feldmann<br>Lindenweg 12<br>38100 Musterstadt</p></div></div>
    <p class="f-news-label">SUBSCRIBE TO OUR NEWSLETTER</p>
    <div class="f-news">ENTER YOUR NEWSLETTER<span class="f-news-go"></span></div>
    <div class="f-media">MEDIA <span class="social"><i></i><i></i><i></i></span></div>
    <p class="f-copy">Copyright@2024 All Rights By ruhiger-morgen</p>
  </footer>
</section>

</div>
</body>
</html>
```